Mesh Banner Design for Business Premises

We require the design of a large mesh banner to be installed across the front fence of our warehouse. The banner should prominently feature our existing Trelborn logo and brand colours (yellow, white, and black) and be designed to be highly visible from the road.

The overall aesthetic should be strong, masculine, and industrial, reflecting the nature of the scaffolding and construction industry. The background should be predominantly black, with our branding incorporated in yellow and white for strong contrast and readability.

The banner should clearly communicate the full scope of services we provide, including:

Scaffold Design
Scaffold Engineering
Scaffold Installation / Erection
Scaffold Dismantling

It should also indicate the types of projects and clients we service, including:

Commercial
Industrial
Residential
Civil

The design should feel bold and professional, with a construction-oriented style that aligns with the scaffolding industry. It should be clean, impactful, and easy to read from a distance, ensuring passing traffic can quickly understand our services.

Where possible, subtle industrial or structural design elements (such as scaffold components, steel textures, or linework) may be incorporated into the background to reinforce the industry theme while keeping the layout uncluttered.

The final design will be produced as a large-format mesh banner for outdoor installation, so it should be created with this application and viewing distance in mind.

```html
<!DOCTYPE html>
<html lang="en">
<head>
<meta charset="utf-8">
<title>Trelborn Mesh Banner</title>
<link href="https://fonts.googleapis.com/css2?family=Saira:wght@500;800&display=swap" rel="stylesheet">
<style>
  :root {
    --stage: #9a9a9a;
    --black: #000000;
    --charcoal: #151515;
    --steel: #262626;
    --yellow: #f9ae1b;
    --white: #ffffff;
  }
  * { margin: 0; padding: 0; box-sizing: border-box; }
  html, body { width: 1200px; height: 716px; overflow: hidden; background: var(--stage); }
  .banner {
    position: absolute; left: 86px; top: 111px; width: 1031px; height: 515px;
    background: radial-gradient(ellipse at 50% 40%, var(--steel) 0%, var(--charcoal) 60%, #0c0c0c 100%);
    box-shadow: 0 4px 14px rgba(0,0,0,0.35);
    font-family: "Saira", sans-serif;
    color: var(--white);
    overflow: hidden;
  }
  .service-band {
    position: absolute; left: 10px; right: 50px; top: 152px; height: 246px;
    background: linear-gradient(90deg, rgba(0,0,0,0.4) 0%, var(--black) 8%, var(--black) 92%, rgba(0,0,0,0.4) 100%);
  }
  .brand-square {
    position: absolute; left: 50%; top: 56px; width: 56px; height: 56px;
    margin-left: -28px; background: var(--yellow);
  }
  .brand-name {
    position: absolute; left: 0; right: 0; top: 145px; text-align: center;
    font-weight: 500; font-size: 24px; letter-spacing: 15px; text-indent: 15px;
    color: var(--white); line-height: 1;
  }
  .brand-feature {
    position: absolute; left: 0; right: 0; top: 238px; text-align: center;
    font-weight: 800; font-size: 76px; line-height: 1; color: var(--yellow);
    letter-spacing: 2px;
  }
  .check-list { position: absolute; list-style: none; }
  .check-list li {
    position: absolute; left: 0; white-space: nowrap;
    font-weight: 800; font-size: 22px; line-height: 1;
  }
  .check-list li svg { position: absolute; left: -26px; top: 3px; width: 17px; height: 17px; }
  .services { left: 77px; top: 0; }
  .sectors { left: 782px; top: 0; }
  .contact {
    position: absolute; top: 416px; left: 0; right: 0; height: 60px;
    font-weight: 800; line-height: 1; white-space: nowrap;
  }
  .contact .icon { position: absolute; top: 13px; }
  .phone-number { position: absolute; left: 122px; top: 2px; font-size: 47px; letter-spacing: 1px; }
  .web-address { position: absolute; left: 486px; top: 2px; font-size: 43px; }
</style>
</head>
<body>
<div class="banner">
  <div class="service-band"></div>

  <span class="brand-square"></span>
  <div class="brand-name">TRELBORN</div>
  <div class="brand-feature">TRELBORN</div>

  <ul class="check-list services">
    <li style="top:188px"><svg viewBox="0 0 16 16"><circle cx="8" cy="8" r="8" fill="#f9ae1b"/><path d="M4.5 8.2l2.4 2.3 4.6-4.8" fill="none" stroke="#000" stroke-width="1.8"/></svg>Scaffold Design</li>
    <li style="top:227px"><svg viewBox="0 0 16 16"><circle cx="8" cy="8" r="8" fill="#f9ae1b"/><path d="M4.5 8.2l2.4 2.3 4.6-4.8" fill="none" stroke="#000" stroke-width="1.8"/></svg>Scaffold Engineering</li>
    <li style="top:267px"><svg viewBox="0 0 16 16"><circle cx="8" cy="8" r="8" fill="#f9ae1b"/><path d="M4.5 8.2l2.4 2.3 4.6-4.8" fill="none" stroke="#000" stroke-width="1.8"/></svg>Scaffold Installation</li>
    <li style="top:294px">/Erection</li>
    <li style="top:334px"><svg viewBox="0 0 16 16"><circle cx="8" cy="8" r="8" fill="#f9ae1b"/><path d="M4.5 8.2l2.4 2.3 4.6-4.8" fill="none" stroke="#000" stroke-width="1.8"/></svg>Scaffold Dismantling</li>
  </ul>

  <ul class="check-list sectors">
    <li style="top:188px"><svg viewBox="0 0 16 16"><circle cx="8" cy="8" r="8" fill="#f9ae1b"/><path d="M4.5 8.2l2.4 2.3 4.6-4.8" fill="none" stroke="#000" stroke-width="1.8"/></svg>Commercial</li>
    <li style="top:238px"><svg viewBox="0 0 16 16"><circle cx="8" cy="8" r="8" fill="#f9ae1b"/><path d="M4.5 8.2l2.4 2.3 4.6-4.8" fill="none" stroke="#000" stroke-width="1.8"/></svg>Industrial</li>
    <li style="top:287px"><svg viewBox="0 0 16 16"><circle cx="8" cy="8" r="8" fill="#f9ae1b"/><path d="M4.5 8.2l2.4 2.3 4.6-4.8" fill="none" stroke="#000" stroke-width="1.8"/></svg>Residential</li>
    <li style="top:337px"><svg viewBox="0 0 16 16"><circle cx="8" cy="8" r="8" fill="#f9ae1b"/><path d="M4.5 8.2l2.4 2.3 4.6-4.8" fill="none" stroke="#000" stroke-width="1.8"/></svg>Civil</li>
  </ul>

  <div class="contact">
    <svg class="icon" style="left:72px" width="34" height="34" viewBox="0 0 24 24" aria-hidden="true">
      <path fill="#f9ae1b" d="M6.6 2.5l3 3.6-1.8 2.3c1.2 2.7 3.1 4.6 5.8 5.8l2.3-1.8 3.6 3-2 3.3c-.4.6-1.1.9-1.8.7C9 17.7 4.3 13 2.6 6.3c-.2-.7.1-1.4.7-1.8z"/>
      <path fill="none" stroke="#f9ae1b" stroke-width="1.3" d="M14 2.5a7.5 7.5 0 0 1 7.5 7.5M14 5.5a4.5 4.5 0 0 1 4.5 4.5"/>
    </svg>
    <span class="phone-number">1300 555 017</span>
    <svg class="icon" style="left:446px" width="33" height="33" viewBox="0 0 24 24" aria-hidden="true">
      <circle cx="12" cy="12" r="10.5" fill="none" stroke="#f9ae1b" stroke-width="2"/>
      <ellipse cx="12" cy="12" rx="4.5" ry="10.5" fill="none" stroke="#f9ae1b" stroke-width="1.6"/>
      <path d="M1.5 12h21M3 7h18M3 17h18M12 1.5v21" stroke="#f9ae1b" stroke-width="1.6"/>
    </svg>
    <span class="web-address">www.trelborn.com.au</span>
  </div>
</div>
</body>
</html>
```